Business Card Design Project

I am looking for a business card design for my custom Audio/Video & Contracting business named Brindlemoor Systems Inc. We do not currently have a corporate logo so you should not feel constrained to work around an existing design. Your design should be elegant and clean while artistically conveying that we are a technology company. We provide A/V services for the commercial and residential markets and contracting services for residential remodeling and home theater construction. We do not have a particular color that we are looking to design around so feel free to be creative.

To get references of the kind of work that we do and design inspiration please visit the following sites:

http://www.velqorant.us
www.pelmotrix.com
www.quillharborinc.com

Reason: I think we are getting close on a couple of the designs and want to give additional time to get tweaks done and to resubmit your designs.

Target Market(s)

Most of our clients are very wealthy and have been exposed to premium brand names in every aspect of their lives, (ie. - luxury autos, estate sized homes, fine jewelery and clothes) and your design needs to convey that same level of excellent design that they are used to.

Industry/Entity Type

Residential

Requirements
Should not have
• An extensive use of the color RED.

```html
<!DOCTYPE html>
<html lang="en">
<head>
<meta charset="utf-8">
<title>Brindlemoor Systems Inc. – Business Card</title>
<link href="https://fonts.googleapis.com/css2?family=Source+Sans+3:wght@400&display=swap" rel="stylesheet">
<style>
  :root {
    --page: #ffffff;
    --frame: #9a9a9a;
    --card: #000000;
    --ink: #ffffff;
    --steel: #9aa6b8;
    --rule: #8c8c8c;
    --mark: #4f6fa8;
  }
  * { box-sizing: border-box; margin: 0; padding: 0; }
  html, body { width: 1200px; height: 900px; overflow: hidden; background: var(--page); }
  body { font-family: "Source Sans 3", "Helvetica Neue", Arial, sans-serif; }
  .canvas {
    position: relative; width: 1200px; height: 900px;
    border: 1px solid var(--frame); border-radius: 6px; background: var(--page);
  }
  .card {
    position: absolute; left: 77px; top: 111px; width: 1046px; height: 677px;
    background: var(--card); color: var(--ink);
  }
  .brand-dot {
    position: absolute; left: 99px; top: 42px; width: 170px; height: 170px;
    border-radius: 50%; background: var(--mark);
  }
  .brand-name {
    position: absolute; left: 340px; top: 82px; width: 604px;
    font-size: 39px; letter-spacing: 1.5px; text-transform: uppercase;
    color: var(--steel); white-space: nowrap; line-height: 1;
  }
  .brand-rule {
    position: absolute; left: 340px; top: 138px; width: 304px; height: 3px; background: var(--rule);
  }
  .brand-tagline {
    position: absolute; left: 656px; top: 122px; width: 288px; text-align: right;
    font-size: 31px; letter-spacing: 2px; color: var(--rule); line-height: 1;
  }
  .holder-name {
    position: absolute; left: 0; right: 0; top: 342px; text-align: center;
    font-size: 50px; line-height: 1;
  }
  .address {
    position: absolute; left: 71px; top: 512px;
    font-size: 26px; line-height: 42px;
  }
  .contact {
    position: absolute; right: 75px; top: 517px; text-align: right;
    font-size: 27px; line-height: 42px;
  }
</style>
</head>
<body>
  <div class="canvas">
    <section class="card">
      <div class="brand-dot" aria-hidden="true"></div>
      <div class="brand-name">Brindlemoor Systems Inc</div>
      <div class="brand-rule"></div>
      <div class="brand-tagline">A/V SERVICES</div>

      <h1 class="holder-name" style="font-weight:400">Dale Hurst</h1>

      <div class="address">
        <div>Adress:................................</div>
        <div>...............................................</div>
        <div>...............................................</div>
      </div>

      <div class="contact">
        <div>Tel: 00345 555 014</div>
        <div>e-mail: dale.hurst@brindlemoor.net</div>
        <div>www.brindlemooraudio.net</div>
      </div>
    </section>
  </div>
</body>
</html>
```